Business Card Design 2018 Pinecrest Machining

Hello,

We need a business card design to reflect our new website we just had designed ( http://www.pinecrestmachining.example/)

We are a growing machine shop looking to grow our clientele and are hoping to update our current business card design to match our website and industry

The colours and design of our website should match to achieve what we are looking for.

I have attached a few images for reference as well as our logo and ISO 9000 needs to be apparent on the card as well

Please let me know what you have :)
Please copy melanie@pinecrestmachining.example on all communication regarding this project

Thanks !!!

Industry/Entity Type

Business

Contact Information for Business Card

Company Name, employee name and title and contact details

Colors
f78f20
ffffff
00a990

Requirements
Must have
• Our logo, Iso 9000 same colours as our website http://www.pinecrestmachining.example/

```html
<!DOCTYPE html>
<html lang="en">
<head>
<meta charset="utf-8">
<title>Pinecrest Machining – Business Card</title>
<link href="https://fonts.googleapis.com/css2?family=Rajdhani:wght@500;600;700&display=swap" rel="stylesheet">
<style>
  :root {
    --card-black: #050505;
    --orange: #f78f20;
    --teal: #00a990;
    --white: #ffffff;
    --ghost: #1c1c1c;
    --backdrop: #e9e6e1;
  }
  * { box-sizing: border-box; margin: 0; padding: 0; }
  html, body {
    width: 1200px; height: 800px; overflow: hidden;
    background: var(--backdrop);
    font-family: "Rajdhani", sans-serif;
  }
  .canvas { position: relative; width: 1200px; height: 800px; }

  .card {
    position: absolute;
    width: 540px; height: 310px;
    background: var(--card-black);
    color: var(--white);
    box-shadow: 0 10px 28px rgba(0,0,0,0.25);
    overflow: hidden;
  }

  /* Logo side */
  .card--logo { left: 50px; top: 90px; }
  .accent-bar { position: absolute; width: 16px; background: var(--orange); }
  .accent-bar--top-right { right: 0; top: 24px; height: 118px; }
  .accent-bar--bottom-left { left: 0; bottom: 34px; height: 118px; }
  .brand {
    position: absolute; left: 0; right: 0; top: 112px;
    display: flex; align-items: center; justify-content: center; gap: 14px;
  }
  .brand-mark { width: 34px; height: 34px; background: var(--white); }
  .brand-name {
    font-weight: 700; font-size: 40px; letter-spacing: 1px;
    text-transform: uppercase; color: var(--white);
  }
  .website {
    position: absolute; left: 0; right: 0; bottom: 42px;
    text-align: center; font-weight: 600; font-size: 19px; color: var(--white);
  }

  /* Contact side */
  .card--contact { left: 610px; top: 400px; }
  .arm-decoration {
    position: absolute; left: 110px; top: 20px; width: 300px; height: 210px;
    background: radial-gradient(ellipse at center, var(--ghost) 0%, rgba(28,28,28,0.4) 60%, transparent 80%);
  }
  .person { position: absolute; left: 22px; top: 22px; padding-left: 14px; }
  .person::before {
    content: ""; position: absolute; left: 0; top: 2px; width: 5px; height: 46px;
    background: var(--teal);
  }
  .person-name { font-weight: 700; font-size: 27px; color: var(--orange); line-height: 1; }
  .person-title { font-weight: 500; font-size: 15px; color: var(--white); margin-top: 3px; }

  .cert-badge {
    position: absolute; right: 30px; top: 82px; width: 150px; height: 66px;
    border: 2px solid var(--white); border-radius: 4px;
  }

  .contacts { position: absolute; left: 28px; top: 184px; list-style: none; }
  .contacts li {
    display: flex; align-items: center; gap: 10px;
    font-weight: 500; font-size: 16px; line-height: 22px; color: var(--white);
  }
  .contacts svg { width: 13px; height: 13px; fill: var(--orange); flex: none; }

  .address {
    position: absolute; right: 22px; bottom: 26px; padding-right: 14px;
    text-align: right; font-style: normal;
    font-weight: 500; font-size: 16px; line-height: 20px; color: var(--white);
  }
  .address::after {
    content: ""; position: absolute; right: 0; top: 2px; width: 5px; height: 38px;
    background: var(--teal);
  }
</style>
</head>
<body>
<div class="canvas">

  <section class="card card--logo" aria-label="Business card, logo side">
    <span class="accent-bar accent-bar--top-right"></span>
    <span class="accent-bar accent-bar--bottom-left"></span>
    <div class="brand">
      <span class="brand-mark"></span>
      <span class="brand-name">Pinecrest Machining</span>
    </div>
    <p class="website">www.pinecrestmachining.example</p>
  </section>

  <section class="card card--contact" aria-label="Business card, contact side">
    <div class="arm-decoration" role="img" aria-label="Faint industrial robot arm decoration"></div>

    <div class="person">
      <h1 class="person-name">Daniel Reyes</h1>
      <p class="person-title">Vice President</p>
    </div>

    <div class="cert-badge" role="img" aria-label="Quality certification badge"></div>

    <ul class="contacts">
      <li>
        <svg viewBox="0 0 24 24" aria-hidden="true"><path d="M6.6 10.8a15.1 15.1 0 0 0 6.6 6.6l2.2-2.2a1 1 0 0 1 1-.25 11.4 11.4 0 0 0 3.6.57 1 1 0 0 1 1 1V20a1 1 0 0 1-1 1A17 17 0 0 1 3 4a1 1 0 0 1 1-1h3.5a1 1 0 0 1 1 1c0 1.25.2 2.45.57 3.6a1 1 0 0 1-.25 1z"/></svg>
        555 010 4827
      </li>
      <li>
        <svg viewBox="0 0 24 24" aria-hidden="true"><path d="M6 2h9l3 3v4H6zM3 10h18a1 1 0 0 1 1 1v7h-4v4H6v-4H2v-7a1 1 0 0 1 1-1zm5 6v4h8v-4z"/></svg>
        555 010 7392
      </li>
      <li>
        <svg viewBox="0 0 24 24" aria-hidden="true"><path d="M2 5h20v14H2zm2 2v.5l8 5 8-5V7l-8 5z"/></svg>
        melanie@pinecrestmachining.example
      </li>
    </ul>

    <address class="address">
      1420 Cedar Row NW<br>
      Alderton, AB&nbsp; T0X 1A1
    </address>
  </section>

</div>
</body>
</html>
```